Wine labels Velmora Wine Council - Nueva etiqueta El Consejo Regulador de vinos de Albarrán

Velmora Wines Council, based in southern Spain, are looking to create a new suite of wine labels which retain the elegance of the Velmora Wines industry while reinvigorating their image to the modern era and a new generation of Sherry Wine lovers. These labels will be used across the Velmora Wines Council's range of wines for the promotion of the Velmora Wines industry.

Your design must present at least two styles of Velmora Wines which demonstrate an elegant, modern interpretation and understanding of the unique mood and personality for these wines and the essence of southern Spain.

10 labels will be created based on the winning design, one for each of the unique varieties of Velmora Wines within the collection. This collection comprises of several different wine varieties including: Fino, Manzanilla, Amontillado, Oloroso, Palo Cortado, Medium, Cream, Pale Cream, Pedro Ximenez and Moscatel.

We recommend you visit our website www.velmora-vinos.example/wines as the source to understanding the origins and unique personality of these diverse wines.

El Consejo Regulador de los Vinos de Albarrán y Tordesal quiere renovar las etiquetas de los vinos utilizados para sus actividades de promoción genérica. Esta colección de vinos comprende las tipologías más importantes de la región que incluye: fino, manzanilla, amontillado, oloroso, palo cortado, pale cream, medium, cream, pedro ximénez y moscatel. Por lo tanto se precisan 10 etiquetas, una para cada uno de los vinos mencionados.
Updates

Project Deadline Extended
Reason: Due to some confusion with the deadline we wish to officially extend the deadline to allow designers one last week to submit their entries.

Target Market(s)

Industry, journalists, media, sommeliers, chefs, wine writers

Industry/Entity Type

Council

Requirements
Must have
• Front and Back label plus capsule:
• Front label can have either of the two official logos of the Velmora Wine council titled Vinos de Albarrán Digital or not, this is optional. Must include: Vino selecionado por el Consejo Regulador de la Denominacion de Origen, Name of the variety of wine eg FINO, percentage of alcohol eg 15% and quantity 75 cl.
• The back of the label must include the council logo titled Sellora and 4 additional logos positioned smaller. The Europa logo must appear larger than the 3 other logos. Space for descriptive text about the wine is also required.
• The dimensions of the bottle can be found at this link http://www.vidrialto.example/es/catalogo/vinos-y-espumosos/bordelesas/bd-orla
• Altura:305 mm
• Diámetro base:76,20 mm
• Diámetro hombro:82 mm
• Tipo boca:Cetie
• Peso:750 gr
• Capacidad:75 cl
• Etiqueta delantera y trasera y capsula
• La etiqueta delantera puede incluir el logo oficial del Consejo Regulador o el logo digital, o ninguno, esto es opcional. Debe incluir el siguiete texto: Vino selecionado por el Consejo Regulador de la Denominacion de Origen, el nombre de la variedad del vino, por ejemplo Fino, el porcentaje de alcohol, por ejemplo 15%, y la capacidad 75cl.
• La etiqueta trasera debe incluir el logo oficial Sellora del Consejo, y cuatro logos adicionales con una dimension menor. El Logo de ¨Europa invierte en las zonas rurales¨ debe ser de mayor tamaño que los otros. Se precisa espacio para el texto descriptivo de los vinos.
• Las dimensiones de la botella se puede encontrar en este enlace
• http://www.vidrialto.example/es/catalogo/vinos-y-espumosos/bordelesas/bd-orla
• Altura:305 mm
• Diámetro base:76,20 mm
• Diámetro hombro:82 mm
• Tipo boca:Cetie
• Peso:750 gr
• Capacidad:75 cl
Nice to have
• See our website velmora-vinos.example to understand the origin of the wines. Ver nuestra página web velmora-vinos.example para mejor entender los vinos.
Should not have
• Images of catavinos or stereotypical images from Spain such as flamenco dancers or guitars.

```html
<!DOCTYPE html>
<html lang="es">
<head>
<meta charset="utf-8">
<title>Vinos de Albarrán – Velmora Wines labels</title>
<link rel="stylesheet" href="https://fonts.googleapis.com/css2?family=Bodoni+Moda:wght@400;500;700&family=Montserrat:wght@400;500&display=swap">
<style>
  :root {
    --backdrop: #b1b0b5;
    --paper: #ffffff;
    --ink: #111111;
    --manzanilla-tab: #f0df8e;
    --manzanilla-wash: #f4e5a2;
    --manzanilla-wash-edge: #f8eec4;
    --oloroso-tab: #4a1010;
    --oloroso-wash: #7c2c23;
    --oloroso-wash-edge: #8f4034;
    --px-tab: #171311;
    --px-wash: #2f2319;
    --px-wash-edge: #46362a;
    --light-type: #ffffff;
  }
  * { box-sizing: border-box; margin: 0; padding: 0; }
  html, body {
    width: 1200px;
    height: 873px;
    overflow: hidden;
    background: var(--backdrop);
  }
  .label-range {
    position: relative;
    width: 1200px;
    height: 873px;
    display: flex;
    justify-content: center;
    align-items: flex-start;
    gap: 90px;
    padding-top: 177px;
  }
  .wine-label {
    position: relative;
    width: 300px;
    height: 519px;
  }
  .label-tab {
    position: absolute;
    left: 110px;
    top: 0;
    width: 80px;
    height: 148px;
    z-index: 2;
  }
  .label-sheet {
    position: absolute;
    left: 0;
    top: 63px;
    width: 300px;
    height: 456px;
    background: var(--paper);
  }
  .brand-name {
    position: absolute;
    top: 114px;
    width: 100%;
    text-align: center;
    font-family: "Bodoni Moda", serif;
    font-weight: 400;
    font-size: 26px;
    letter-spacing: -0.5px;
    color: var(--ink);
  }
  .brand-sub {
    position: absolute;
    top: 151px;
    width: 100%;
    text-align: center;
    font-family: "Montserrat", sans-serif;
    font-weight: 500;
    font-size: 12px;
    letter-spacing: 3.2px;
    color: var(--ink);
  }
  .wash {
    position: absolute;
    left: 0;
    top: 214px;
    width: 300px;
    height: 180px;
  }
  .wash-type {
    position: absolute;
    top: 268px;
    width: 100%;
    text-align: center;
  }
  .wine-class {
    font-family: "Montserrat", sans-serif;
    font-weight: 400;
    font-size: 14px;
    letter-spacing: 0.8px;
  }
  .wine-name {
    margin-top: 4px;
    font-family: "Bodoni Moda", serif;
    font-weight: 700;
    font-size: 31px;
    line-height: 1.05;
    letter-spacing: 1.6px;
  }
  .wine-label--manzanilla .wash-type { color: var(--ink); }
  .wine-label--oloroso .wash-type,
  .wine-label--px .wash-type { color: var(--light-type); }
  .wine-label--px .wash-type { top: 252px; }
  .label-facts {
    position: absolute;
    left: 14px;
    right: 14px;
    bottom: 10px;
    display: flex;
    justify-content: space-between;
    align-items: baseline;
    font-family: "Bodoni Moda", serif;
    color: var(--ink);
  }
  .fact-volume, .fact-strength { font-size: 15px; }
  .fact-vintage { font-size: 20px; font-weight: 700; letter-spacing: 0.5px; }
</style>
</head>
<body>
<main class="label-range">

  <article class="wine-label wine-label--manzanilla">
    <svg class="label-tab" viewBox="0 0 80 148" role="img" aria-label="Tab with line-drawn wine glass emblem">
      <rect width="80" height="148" fill="var(--manzanilla-tab)"/>
    </svg>
    <div class="label-sheet">
      <p class="brand-name">VINOS DE ALBARRÁN</p>
      <p class="brand-sub">VELMORA WINES</p>
      <svg class="wash" viewBox="0 0 300 180" preserveAspectRatio="none" role="img" aria-label="Pale yellow brush-stroke band with faint sunburst pattern">
        <defs>
          <linearGradient id="wash-manzanilla" x1="0" y1="0" x2="0" y2="1">
            <stop offset="0" stop-color="var(--manzanilla-wash-edge)"/>
            <stop offset="0.25" stop-color="var(--manzanilla-wash)"/>
            <stop offset="0.85" stop-color="var(--manzanilla-wash)"/>
            <stop offset="1" stop-color="var(--manzanilla-wash-edge)"/>
          </linearGradient>
        </defs>
        <rect width="300" height="180" fill="url(#wash-manzanilla)"/>
      </svg>
      <div class="wash-type">
        <p class="wine-class">VINO GENEROSO</p>
        <p class="wine-name">MANZANILLA</p>
      </div>
      <div class="label-facts">
        <span class="fact-volume">75cl</span>
        <span class="fact-vintage">2014</span>
        <span class="fact-strength">15% vol.</span>
      </div>
    </div>
  </article>

  <article class="wine-label wine-label--oloroso">
    <svg class="label-tab" viewBox="0 0 80 148" role="img" aria-label="Tab with line-drawn wine glass emblem">
      <rect width="80" height="148" fill="var(--oloroso-tab)"/>
    </svg>
    <div class="label-sheet">
      <p class="brand-name">VINOS DE ALBARRÁN</p>
      <p class="brand-sub">VELMORA WINES</p>
      <svg class="wash" viewBox="0 0 300 180" preserveAspectRatio="none" role="img" aria-label="Deep red-brown brush-stroke band with faint sunburst pattern">
        <defs>
          <linearGradient id="wash-oloroso" x1="0" y1="0" x2="0" y2="1">
            <stop offset="0" stop-color="var(--oloroso-wash-edge)"/>
            <stop offset="0.2" stop-color="var(--oloroso-wash)"/>
            <stop offset="0.85" stop-color="var(--oloroso-wash)"/>
            <stop offset="1" stop-color="var(--oloroso-wash-edge)"/>
          </linearGradient>
        </defs>
        <rect width="300" height="180" fill="url(#wash-oloroso)"/>
      </svg>
      <div class="wash-type">
        <p class="wine-class">VINO GENEROSO</p>
        <p class="wine-name">OLOROSO</p>
      </div>
      <div class="label-facts">
        <span class="fact-volume">75cl</span>
        <span class="fact-vintage">2014</span>
        <span class="fact-strength">15% vol.</span>
      </div>
    </div>
  </article>

  <article class="wine-label wine-label--px">
    <svg class="label-tab" viewBox="0 0 80 148" role="img" aria-label="Tab with line-drawn wine glass emblem">
      <rect width="80" height="148" fill="var(--px-tab)"/>
    </svg>
    <div class="label-sheet">
      <p class="brand-name">VINOS DE ALBARRÁN</p>
      <p class="brand-sub">VELMORA WINES</p>
      <svg class="wash" viewBox="0 0 300 180" preserveAspectRatio="none" role="img" aria-label="Dark brown printed-texture band with tally-mark edge">
        <defs>
          <linearGradient id="wash-px" x1="0" y1="0" x2="0" y2="1">
            <stop offset="0" stop-color="var(--px-wash-edge)"/>
            <stop offset="0.2" stop-color="var(--px-wash)"/>
            <stop offset="0.9" stop-color="var(--px-wash)"/>
            <stop offset="1" stop-color="var(--px-wash-edge)"/>
          </linearGradient>
        </defs>
        <rect width="300" height="180" fill="url(#wash-px)"/>
      </svg>
      <div class="wash-type">
        <p class="wine-class">VINO GENEROSO</p>
        <p class="wine-name">PEDRO<br>XIMENÉZ</p>
      </div>
      <div class="label-facts">
        <span class="fact-volume">75cl</span>
        <span class="fact-vintage">2014</span>
        <span class="fact-strength">15% vol.</span>
      </div>
    </div>
  </article>

</main>
</body>
</html>
```